Risk Management Company in need of Business Card Design

We sell risk management insurance to Lenders (Banks, Credit Unions, Real Estate Trust).

We need a very clean, professional card that will leave a great impression.

We are looking to use a blue color for our logo on the card (Preferably close to royal blue but are open to looking at navy blue or any darker blues as well).

Please see the logo attached to get an idea. We are open to writing Harbor Shield Under the logo or next to the logo. Really whatever looks best.

Target Market(s)

Banks, Credit Unions, Real Estate Trusts

Industry/Entity Type

Insurance

Contact Information for Business Card

Name: Mark Dunstan
Title: Regional Sales Director
Email: mdunstan@harborshield.example
C:410-555-0143
D:410-555-0187
888-555-0129 Ext.205
F:443-555-0164 (We would like to see some cards without the fax number as well to compare)

Company Name: Harbor Shield
Website: www.harborshield.example

Address: 118 E. Morrow St. Suite 420, Towson, MD 21299 (Preferably written on the bottom of the card in small print.)

Colors
0355a3
0455a3

Requirements
Nice to have
• We would like to see a couple of where the back has the logo in reverse colors (Logo White, Background Blue)

```html
<!DOCTYPE html>
<html lang="en">
<head>
<meta charset="utf-8">
<title>Harbor Shield — Business Card</title>
<link rel="stylesheet" href="https://fonts.googleapis.com/css2?family=PT+Sans+Narrow:wght@400;700&display=swap">
<style>
  :root {
    --brand-blue: #30358f;
    --ink: #4a4a4f;
    --ink-soft: #6a6a70;
    --paper: #ffffff;
    --backdrop: #e6e6e8;
  }
  html, body {
    margin: 0;
    padding: 0;
    width: 1200px;
    height: 1000px;
    overflow: hidden;
    background: var(--backdrop);
    font-family: "PT Sans Narrow", "Arial Narrow", sans-serif;
  }
  .canvas {
    position: relative;
    width: 1200px;
    height: 1000px;
  }
  .business-card {
    position: absolute;
    left: 180px;
    top: 260px;
    width: 840px;
    height: 480px;
    background: var(--paper);
    box-shadow: 0 10px 30px rgba(0,0,0,0.12);
    overflow: hidden;
  }
  .brand {
    position: absolute;
    left: 60px;
    top: 150px;
    width: 320px;
    text-align: center;
  }
  .brand-mark {
    display: block;
    margin: 0 auto 18px;
  }
  .brand-name {
    margin: 0;
    color: var(--brand-blue);
    font-size: 46px;
    font-weight: 400;
    letter-spacing: 2px;
    text-transform: uppercase;
    line-height: 1;
  }
  .website {
    position: absolute;
    left: 60px;
    top: 392px;
    width: 320px;
    text-align: center;
    color: var(--ink-soft);
    font-size: 21px;
  }
  .contact-block {
    position: absolute;
    left: 420px;
    top: 52px;
    color: var(--ink);
  }
  .person-name {
    margin: 0;
    color: var(--brand-blue);
    font-size: 30px;
    font-weight: 700;
    line-height: 1.05;
  }
  .person-title {
    margin: 2px 0 0;
    color: var(--ink-soft);
    font-size: 21px;
  }
  .contact-list {
    list-style: none;
    margin: 38px 0 0;
    padding: 0;
    font-size: 21px;
    line-height: 25px;
  }
  .address {
    position: absolute;
    left: 540px;
    top: 350px;
    margin: 0;
    font-style: normal;
    color: var(--ink-soft);
    font-size: 21px;
    line-height: 25px;
  }
  .accent-bar {
    position: absolute;
    right: 0;
    bottom: 0;
    width: 330px;
    height: 26px;
    background: var(--brand-blue);
  }
</style>
</head>
<body>
<main class="canvas">
  <article class="business-card">
    <div class="brand">
      <svg class="brand-mark" width="84" height="84" viewBox="0 0 84 84" aria-hidden="true">
        <circle cx="42" cy="42" r="42" fill="var(--brand-blue)"/>
      </svg>
      <h1 class="brand-name">Harbor Shield</h1>
    </div>
    <div class="website">www.harborshield.example</div>

    <section class="contact-block">
      <h2 class="person-name">Mark Dunstan</h2>
      <p class="person-title">Regional Sales Director</p>
      <ul class="contact-list">
        <li>D: 410-555-0187</li>
        <li>C: 410-555-0143</li>
        <li>443-555-0164 Ext. 255</li>
        <li>888-555-0129 Ext. 255</li>
        <li>mdunstan@harborshield.example</li>
      </ul>
    </section>

    <address class="address">
      118 E. Morrow St. Suite 420<br>
      Towson, MD 21299
    </address>

    <div class="accent-bar"></div>
  </article>
</main>
</body>
</html>
```